One-page brochure for online auction company

We are seeking a designed to take the attached PDF and make it into a professional one-page, two-sided, full bleed 8.5x11" brochure with photo graphics. The product will be professionally printed and distributed to potential customers.

We're an online auction company that specializes in serving commercial printers for their equipment needs. Feel free to browse our website for inspiration and photos to use on the brochure. http://www.lotvane.com.

The vector format of the logo is available on request, but should also be embedded in the PDF attached.

The design of this brochure should reflect the industrial nature of the industry.

We would like most of the information on the PDF to make it to the brochure but if there is not enough room, we are willing to eliminate some.

Target Market(s)

Commercial print shops and printing equipment dealers

Industry/Entity Type

Printing

Font styles to use
Sans Serif

Requirements
Must have
• At least most of the copy on the provided PDF
Nice to have
• Large photos of printing presses and other equipment, designer's chocie

```html
<!DOCTYPE html>
<html lang="en">
<head>
<meta charset="utf-8">
<title>Auction Brochure Panel</title>
<link rel="stylesheet" href="https://fonts.googleapis.com/css2?family=Montserrat:wght@600;700&family=Hind:wght@400;500&display=swap">
<style>
  :root {
    --paper: #ffffff;
    --ink: #2f2f2f;
    --accent: #ef8a22;
    --green: #5e9a7c;
    --green-soft: rgba(94, 154, 124, 0.55);
    --photo-dark: #4a5a5a;
    --photo-mid: #7f9593;
    --photo-light: #c9d3d0;
  }
  * { margin: 0; padding: 0; box-sizing: border-box; }
  html, body { width: 1200px; height: 928px; overflow: hidden; background: var(--paper); }
  .page { position: relative; width: 1200px; height: 928px; background: var(--paper); overflow: hidden; font-family: "Hind", Arial, sans-serif; color: var(--ink); }

  .photo { position: absolute; }
  .photo--cutter { left: 532px; top: 0; width: 668px; height: 461px;
    background: linear-gradient(135deg, var(--photo-mid) 0%, var(--photo-dark) 55%, #2f3a3d 100%); }
  .photo--folder { left: 0; top: 500px; width: 620px; height: 428px;
    background: linear-gradient(160deg, var(--photo-light) 0%, var(--photo-mid) 45%, #3d6f86 100%); }

  .shapes { position: absolute; inset: 0; width: 1200px; height: 928px; pointer-events: none; }

  .section { position: absolute; }
  .section--targeting { left: 28px; top: 40px; width: 500px; }
  .section--userbase { left: 646px; top: 558px; width: 530px; }
  .section--pricing { left: 646px; top: 718px; width: 520px; }

  .section__title { font-family: "Montserrat", Arial, sans-serif; font-weight: 700; color: var(--accent);
    font-size: 25px; line-height: 1.1; letter-spacing: 0.2px; margin-bottom: 6px; text-transform: uppercase; }
  .section__intro { font-size: 19px; line-height: 1.3; margin-bottom: 6px; }

  .steps { list-style: none; }
  .steps__item { position: relative; padding-left: 36px; font-size: 19px; line-height: 1.3; margin-bottom: 6px; }
  .steps__num { position: absolute; left: 0; top: 0; width: 26px; height: 26px; border-radius: 50%;
    background: var(--accent); color: var(--paper); font-weight: 500; font-size: 20px; line-height: 29px; text-align: center; }
  .section__body { font-size: 19px; line-height: 1.3; }
</style>
</head>
<body>
<main class="page">
  <div class="photo photo--cutter" role="img" aria-label="Photo of an operator at an industrial paper guillotine cutter with a stack of paper"></div>
  <div class="photo photo--folder" role="img" aria-label="Photo of a blue paper folding machine on a print shop floor"></div>

  <svg class="shapes" viewBox="0 0 1200 928" aria-hidden="true">
    <polygon points="532,0 760,0 532,300" fill="var(--green-soft)"/>
    <polygon points="900,461 1200,461 1200,240" fill="rgba(94,154,124,0.35)"/>
    <polygon points="1045,461 1200,461 1200,560" fill="var(--green)"/>
    <polygon points="0,378 0,500 228,500" fill="var(--green)"/>
    <polygon points="0,500 220,500 0,700" fill="rgba(94,154,124,0.35)"/>
    <polygon points="620,700 620,928 430,928" fill="rgba(94,154,124,0.4)"/>
  </svg>

  <section class="section section--targeting">
    <h2 class="section__title">Effective Target Marketing</h2>
    <p class="section__intro">Boosting each seller’s opportunity for reaching potential auction bidders by:</p>
    <ol class="steps">
      <li class="steps__item"><span class="steps__num">1</span>Communicating to 64,000 recipients, all likely purchasers of industrial equipment, via two email blasts, the value of purchasing your asset</li>
      <li class="steps__item"><span class="steps__num">2</span>Securing a 25-30% open rate on each email campaign</li>
      <li class="steps__item"><span class="steps__num">3</span>Featuring your auction on the front page of our website</li>
      <li class="steps__item"><span class="steps__num">4</span>Seeking out trade websites specific to the items being sold</li>
      <li class="steps__item"><span class="steps__num">5</span>Listing expansion to additional targeted markets available</li>
    </ol>
  </section>

  <section class="section section--userbase">
    <h2 class="section__title">Developing a Broad Userbase</h2>
    <ol class="steps">
      <li class="steps__item"><span class="steps__num">1</span>Expanding over 9,000 users from 119 countries</li>
      <li class="steps__item"><span class="steps__num">2</span>Leveraging an average of 50,000 visitors per month</li>
      <li class="steps__item"><span class="steps__num">3</span>Winning 200,000 pageviews per month</li>
    </ol>
  </section>

  <section class="section section--pricing">
    <h2 class="section__title">No Setup Fee, Commission<br>-Based Pricing</h2>
    <p class="section__body">Our pricing is competitive and requires no up-front commitment from you. Please call us to discuss your auction and the commission options available.</p>
  </section>
</main>
</body>
</html>
```